Energy cost saving website (job description rewritten!)

Job Type: WordPress design
Task Outline: Create a WordPress design
Task Description:
We are new business (Germany) in the market of saving costs by power-saving (name: 'wir-falten-eure-Wolkenbögen.de'). This is reached by changing the supplier, the use of LED bulbs, energy saving washing machines, stoves, microwaves, hairdryers, vacuum cleaners and the like - where all of these be selled or affiliated through the website maybe you will create for us.
Design parameters:
We want a serious design that embodies a feeling of honesty, competence and capability.
Visitors should particularly see that this site saves them money!
The home page mainly should act as a selector of possibilities saving money by power-saving, usage of LED bulbs and large energy saving household devices (washing machines, etc.)
Updates
Hello designers,
browsing through the PixelHarbors files of portfolios I found one header graphics which excites me. Please find it here: http://www.pixelharbor-example.net/design/482716/wordpress-design-by-tarek-olumide . Note: it is NOT the picture but the shadowing. So if you consider this in your concepts would be another 'nice-to-have'.
Thanks.
Target Market(s)
People looking out for saving money by power-saving.
Industry/Entity Type
Business
Requirements
Must have
- Look and feel of 'this site saves me money'!
Nice to have
- We love 3D effects, but its not a must have. We also like cartoons, but feel free to develop your own concept, please. An appropriate backgrond picture would be nice.
Should not have
- Some kind of these exaggerated smiling or handshaking photos. That bathetic symbols like money bills or coins stacks.

```html
<!DOCTYPE html>
<html lang="de">
<head>
<meta charset="utf-8">
<title>wir-falten-eure-Wolkenbögen.de</title>
<link rel="stylesheet" href="https://fonts.googleapis.com/css2?family=Open+Sans:wdth,wght@75,300;75,400&display=swap">
<style>
  :root {
    --page-bg: #e6e6e6;
    --header-top: #9c9c9c;
    --header-bottom: #cfcfcf;
    --teal: #1f7262;
    --teal-dark: #1c6a5b;
    --gold: #f0b433;
    --orange: #ff5a36;
    --orange-soft: #ff9a3c;
    --slate: #527f91;
    --white: #ffffff;
    --link: #6fe0c4;
    --input-bg: #d9d9d9;
  }
  * { box-sizing: border-box; margin: 0; padding: 0; }
  html, body { width: 1200px; height: 963px; overflow: hidden; }
  body {
    position: relative;
    background: var(--page-bg);
    font-family: "Open Sans", "Arial Narrow", sans-serif;
    font-stretch: 75%;
    font-weight: 300;
    color: var(--white);
  }
  button, input { font-family: inherit; font-stretch: 75%; }
  .site-header {
    position: absolute; left: 0; top: 0; width: 1200px; height: 127px;
    background: linear-gradient(180deg, var(--header-top), var(--header-bottom));
    box-shadow: 0 2px 4px rgba(0,0,0,.15);
  }
  .nav-button {
    position: absolute; top: 36px; height: 55px; width: 119px;
    display: flex; align-items: center; justify-content: center;
    background: var(--teal); border: 3px solid var(--white); border-radius: 3px;
    font-size: 22px; color: var(--white); text-decoration: none; text-transform: uppercase;
  }
  .nav-button.is-active { background: var(--gold); }
  .nav-home { left: 99px; }
  .nav-about { left: 234px; }
  .nav-product { left: 845px; }
  .nav-contact { left: 980px; }

  .logo-badge { position: absolute; left: 385px; top: 0; width: 430px; height: 200px; z-index: 3; }
  .logo-name {
    position: absolute; left: 385px; top: 100px; width: 430px; text-align: center; z-index: 4;
    font-size: 26px; font-weight: 400; color: var(--teal); white-space: nowrap;
  }

  .hero {
    position: absolute; left: 100px; top: 151px; width: 1000px; height: 394px;
    background: #9a9a9a; border-radius: 4px; padding: 5px;
    box-shadow: 0 30px 30px -14px rgba(0,0,0,.35);
  }
  .hero-photo {
    position: relative; width: 100%; height: 100%;
    background: linear-gradient(100deg, #2a3033 0%, #5d6a66 35%, #8c7b6c 55%, #55605d 75%, #2c3134 100%);
  }
  .hero-caption {
    position: absolute; left: 0; bottom: 0; width: 100%; height: 132px;
    background: rgba(0,0,0,.55);
    display: flex; align-items: center; justify-content: center;
    font-size: 36px; font-weight: 300; white-space: nowrap;
  }

  .feature-card { position: absolute; top: 595px; width: 312px; height: 283px; background: var(--slate); }
  .card-providers { left: 99px; }
  .card-led { left: 443px; }
  .card-appliances { left: 786px; }
  .card-title {
    height: 52px; background: var(--orange);
    display: flex; align-items: center; gap: 16px; padding-left: 20px;
    font-size: 31px; font-weight: 300; white-space: nowrap;
  }
  .card-body { padding: 10px 16px 0 26px; font-size: 13.5px; line-height: 23.5px; }
  .card-list { list-style: none; }
  .card-list li { position: relative; padding-left: 24px; }
  .card-list li svg { position: absolute; left: 0; top: 5px; }
  .card-appliances .card-list { margin-top: 23px; }
  .card-button {
    position: absolute; right: 21px; bottom: 11px; height: 31px; padding: 0 11px;
    background: var(--orange-soft); border: 1px solid #c9632a; color: var(--white);
    font-size: 16px; font-weight: 300; line-height: 29px;
  }

  .site-footer {
    position: absolute; left: 0; top: 905px; width: 1200px; height: 58px;
    background: var(--teal-dark); font-size: 15px; white-space: nowrap;
  }
  .footer-copy { position: absolute; left: 117px; top: 19px; }
  .footer-links { position: absolute; left: 304px; top: 19px; color: var(--link); }
  .footer-links a { color: var(--link); text-decoration: none; }
  .footer-links span { margin: 0 10px; }
  .newsletter-input {
    position: absolute; left: 620px; top: 11px; width: 296px; height: 32px;
    background: var(--input-bg); border: none; padding-left: 10px;
    font-size: 14px; font-weight: 300; color: #777;
  }
  .newsletter-button {
    position: absolute; left: 925px; top: 11px; width: 174px; height: 32px;
    background: var(--orange-soft); border: 1px solid #c9632a; color: var(--white);
    font-size: 17px; font-weight: 300; text-transform: uppercase;
  }
</style>
</head>
<body>
<svg width="0" height="0" style="position:absolute">
  <defs>
    <symbol id="icon-bolt" viewBox="0 0 20 34">
      <path d="M3 1 L9 15 L5 16 L16 33 L11 18 L15 17 Z" fill="none" stroke="#f7c23a" stroke-width="2" stroke-linejoin="round"/>
    </symbol>
    <symbol id="icon-spark" viewBox="0 0 14 14">
      <path d="M7 0 L8.4 4.6 L13 3 L9.6 6.6 L14 9 L9 9 L9.5 14 L7 10 L4.5 14 L5 9 L0 9 L4.4 6.6 L1 3 L5.6 4.6 Z" fill="#f7c23a"/>
      <circle cx="7" cy="7.2" r="2.2" fill="#f39a1e"/>
    </symbol>
  </defs>
</svg>

<header class="site-header">
  <a class="nav-button nav-home is-active" href="#">Home</a>
  <a class="nav-button nav-about" href="#">About</a>
  <a class="nav-button nav-product" href="#">Product</a>
  <a class="nav-button nav-contact" href="#">Contact</a>
</header>

<svg class="logo-badge" viewBox="0 0 430 200" aria-hidden="true">
  <defs>
    <linearGradient id="badgeFill" x1="0" y1="0" x2="0" y2="1">
      <stop offset="0" stop-color="#f7f7f7"/>
      <stop offset="1" stop-color="#e4e4e4"/>
    </linearGradient>
  </defs>
  <path d="M64 -4 L366 -4 L424 150 Q436 196 392 196 L38 196 Q-6 196 6 150 Z" fill="url(#badgeFill)" stroke="#f39a3c" stroke-width="3"/>
</svg>
<div class="logo-name">wir-falten-eure-Wolkenbögen.de</div>

<section class="hero">
  <div class="hero-photo" role="img" aria-label="Photo of two business people shaking hands in an office">
    <div class="hero-caption">Effective Communication in the workplace is the backbone of any Business.</div>
  </div>
</section>

<article class="feature-card card-providers">
  <h2 class="card-title"><svg width="20" height="34"><use href="#icon-bolt"/></svg>Anbieterwechsel</h2>
  <div class="card-body">
    <ul class="card-list">
      <li><svg width="14" height="14"><use href="#icon-spark"/></svg>Stromkosten senken durch Anbieterwechsel zu kompliziert?</li>
      <li><svg width="14" height="14"><use href="#icon-spark"/></svg>Anbieterwechsel zu viel Arbeit?</li>
      <li><svg width="14" height="14"><use href="#icon-spark"/></svg>Anbieterwechsel hat einen schlechten Ruf?</li>
      <li><svg width="14" height="14"><use href="#icon-spark"/></svg>Angebote zur Stromkostensenkung zu verwirrend?</li>
      <li><svg width="14" height="14"><use href="#icon-spark"/></svg>AGBs der Stromanbieter undurchschaubar?</li>
      <li><svg width="14" height="14"><use href="#icon-spark"/></svg>Jedes Jahr neu entscheiden und kümmern?</li>
    </ul>
  </div>
  <button class="card-button">zum Rundum-sorglos-Paket</button>
</article>

<article class="feature-card card-led">
  <h2 class="card-title"><svg width="20" height="34"><use href="#icon-bolt"/></svg>LED-Leuchtmittel</h2>
  <div class="card-body">
    <p>Sie sind die Leuchtmittel der Zukunft und so wollen wir auch an dieser Stelle mit gutem Beispiel voran gehen, diese neue TEchnik vorstellen, Ängste und Vorurteile abbauen und LEDs vorstellen und empfehlen. Noch sind sie relativ teuer, sie spielen jedoch ihre Kosten meist in weniger als 2 Jahren wieder herin. Selbstverständlich finden Sie hier auch einen Amortisationsrechner, der Ihnen das genau ausrechnet - Leuchtmittel für Leuchtmittel.</p>
  </div>
</article>

<article class="feature-card card-appliances">
  <h2 class="card-title"><svg width="20" height="34"><use href="#icon-bolt"/></svg>Haushaltsgroßgeräte</h2>
  <div class="card-body">
    <p>Hier lässt sich eine Menge Strom und damit natürlich eben auch Kosten sparen. wir-falten-eure-Wolkenbögen.de stellt Ihnen an dieser Stelle daher die sparsamsten Modelle vor:</p>
    <ul class="card-list">
      <li><svg width="14" height="14"><use href="#icon-spark"/></svg>Waschmaschinen</li>
      <li><svg width="14" height="14"><use href="#icon-spark"/></svg>Waschtrockner</li>
      <li><svg width="14" height="14"><use href="#icon-spark"/></svg>Wäschetrockner</li>
      <li><svg width="14" height="14"><use href="#icon-spark"/></svg>Weinkühlschränke</li>
    </ul>
  </div>
</article>

<footer class="site-footer">
  <div class="footer-copy">© 2012 fold-your-cloudarcs.de</div>
  <nav class="footer-links">
    <a href="#">Privacy Statement</a><span>|</span><a href="#">Imprint</a><span>|</span><a href="#">Contact</a>
  </nav>
  <input class="newsletter-input" type="email" placeholder="Ihre E-Mail-Adresse">
  <button class="newsletter-button">Jetzt Info anfordern!</button>
</footer>
</body>
</html>
```